New Web Design Project

New Roofing Website homepage mockup

Complete design document here: https://files.plorvex.net/doc/7tQmZrA2kLwP9xVbN4cYhE3sJdF8gUoR6iKe1nTy/edit?usp=sharing
Updates

Number of Pages Required

1 page

Font styles to use
Sans Serif

```html
<!DOCTYPE html>
<html lang="en">
<head>
<meta charset="utf-8">
<title>Keystone Roofing — Built Right, Built to Last</title>
<link href="https://fonts.googleapis.com/css2?family=Montserrat:wght@500;600;700;800&family=Open+Sans:wght@400;600&display=swap" rel="stylesheet">
<style>
:root{
  --blue:#1e8ddb;
  --blue-dark:#1673b8;
  --ink:#1d1d1f;
  --text:#444;
  --muted:#777;
  --light:#f4f1f1;
  --white:#fff;
  --footer:#1f1f21;
  --line:#cfcfcf;
}
*{box-sizing:border-box;margin:0;padding:0}
html,body{width:1200px;height:4843px;overflow:hidden}
body{font-family:"Open Sans",Arial,sans-serif;color:var(--text);background:var(--white);position:relative}
section,header,footer{position:absolute;left:0;width:1200px}
.h2{font-family:"Montserrat",Arial,sans-serif;font-weight:700;font-size:23px;color:var(--ink);text-align:center;text-transform:uppercase;position:absolute;left:0;width:1200px}
.h2::after{content:"";display:block;width:34px;height:3px;background:#555;margin:14px auto 0}
.btn{font-family:"Montserrat",Arial,sans-serif;font-weight:700;text-transform:uppercase;background:var(--blue);color:var(--white);display:flex;align-items:center;justify-content:center;position:absolute;letter-spacing:.3px}
.photo{position:absolute}

/* header + hero */
.hero{top:0;height:640px;background:linear-gradient(180deg,#d9e2ec 0%,#c4d2e0 30%,#b8c6d4 50%)}
.hero .photo{left:0;top:300px;width:1200px;height:340px;background:linear-gradient(180deg,#b3bcc4 0%,#8e959b 40%,#6f7c5e 75%,#4f6340 100%)}
.brand{position:absolute;left:132px;top:70px;display:flex;align-items:center;gap:10px}
.brand-mark{width:18px;height:18px;background:var(--blue)}
.brand-name{font-family:"Montserrat",Arial,sans-serif;font-weight:700;font-size:21px;color:var(--blue-dark);letter-spacing:.5px;white-space:nowrap}
.brand-tag{position:absolute;left:132px;top:106px;font-size:8px;letter-spacing:2.5px;color:#6b7a88;text-transform:uppercase}
.follow{position:absolute;left:730px;top:24px;font-family:"Montserrat",sans-serif;font-size:11px;font-weight:600;color:var(--ink)}
.follow .dots{display:flex;gap:6px;margin-top:8px}
.follow .dots span{width:26px;height:26px;border-radius:50%;background:var(--blue-dark)}
.follow .dots span:last-child{background:#1a2f5a}
.call{position:absolute;left:860px;top:24px;font-family:"Montserrat",sans-serif;font-size:11px;font-weight:600;color:var(--ink)}
.call .num{display:flex;align-items:center;gap:6px;margin-top:6px;font-size:25px;font-weight:700;color:var(--blue)}
.call .num svg{width:22px;height:22px}
.nav{position:absolute;left:490px;top:94px;display:flex;gap:30px;font-family:"Montserrat",sans-serif;font-size:13px;font-weight:600;color:var(--ink);text-transform:uppercase}
.nav .active{color:var(--blue);text-decoration:underline}
.hero h1{position:absolute;top:208px;left:0;width:1200px;text-align:center;font-family:"Montserrat",sans-serif;font-weight:700;font-size:29px;color:var(--ink);letter-spacing:.5px}
.hero .btn{left:459px;top:272px;width:282px;height:42px;font-size:15px}

/* services */
.services{top:640px;height:413px;background:var(--white)}
.services .h2{top:48px}
.svc{position:absolute;top:171px;width:269px;height:186px;border:1px solid var(--line);text-align:center}
.svc .ic{position:absolute;left:50%;top:-38px;margin-left:-49px;width:98px;height:98px;border-radius:50%;background:var(--blue);display:flex;align-items:center;justify-content:center}
.svc .ic svg{width:54px;height:54px}
.svc h3{margin-top:90px;font-family:"Montserrat",sans-serif;font-size:14px;font-weight:700;color:var(--ink)}
.svc p{margin-top:14px;font-size:11px;line-height:17px;color:#555}

/* about */
.about{top:1053px;height:399px;background:var(--blue)}
.about .photo{left:132px;top:0;width:481px;height:399px;background:linear-gradient(160deg,#cfd8e2 0%,#a7b1bd 35%,#6f8660 70%,#4e6b3f 100%)}
.about h2{position:absolute;left:667px;top:48px;font-family:"Montserrat",sans-serif;font-size:23px;font-weight:700;color:var(--white)}
.about h2::after{content:"";display:block;width:34px;height:3px;background:var(--white);margin-top:10px}
.about p{position:absolute;left:667px;top:122px;width:393px;font-size:14px;line-height:22.5px;color:#e8f3fc}
.about .btn{left:667px;top:311px;width:114px;height:36px;background:var(--white);color:var(--blue);font-size:12px}

/* roof types */
.roofs{top:1452px;height:707px;background:var(--light)}
.roofs .h2{top:46px}
.tile{position:absolute}
.tile span{position:absolute;left:18px;bottom:16px;font-family:"Montserrat",sans-serif;font-weight:600;font-size:17px;color:var(--white)}
.tile span::before{content:"";display:block;width:70px;height:2px;background:var(--white);margin-bottom:8px;margin-left:-18px}

/* projects */
.projects{top:2159px;height:1029px;background:var(--white)}
.projects .h2{top:70px}
.grid{position:absolute;left:132px;top:149px;width:933px;height:739px;display:grid;grid-template-columns:repeat(4,1fr);grid-template-rows:repeat(2,1fr)}
.grid .photo{position:relative}
.grid .tag{position:absolute;left:50%;top:50%;transform:translate(-50%,-50%);border:2px solid var(--white);padding:6px 14px;font-family:"Montserrat",sans-serif;font-weight:700;font-size:13px;color:var(--white)}
.projects .btn{left:510px;top:929px;width:178px;height:36px;font-size:12px}

/* estimate */
.estimate{top:3188px;height:715px;background:var(--light)}
.estimate .h2{top:60px}
.steps{position:absolute;left:130px;top:138px;display:flex;gap:13px}
.step{width:227px;height:64px;background:var(--white);border:1px solid var(--line);display:flex;align-items:center;gap:10px;padding-left:16px;font-family:"Montserrat",sans-serif;font-size:13px;font-weight:700;color:var(--ink);text-transform:uppercase}
.step i{width:24px;height:24px;border-radius:50%;background:var(--blue);color:var(--white);font-style:normal;font-size:11px;display:flex;align-items:center;justify-content:center}
.step.on{background:var(--blue);color:var(--white);border-color:var(--blue)}
.step.on i{background:var(--white);color:var(--blue)}
.estimate h3{position:absolute;top:260px;left:0;width:1200px;text-align:center;font-family:"Montserrat",sans-serif;font-size:18px;font-weight:700;color:var(--ink);text-transform:uppercase}
.products{position:absolute;left:23px;top:339px;display:flex;gap:15px}
.prod{width:181px;height:329px;background:var(--white)}
.prod .photo{position:relative;height:152px}
.prod .body{padding:16px 18px 0}
.prod .tier{font-size:10px;color:#555;text-transform:uppercase}
.prod .name{font-family:"Montserrat",sans-serif;font-size:10px;font-weight:700;color:var(--ink);text-transform:uppercase;margin-top:4px;line-height:12px;min-height:24px}
.prod .price{font-family:"Montserrat",sans-serif;font-size:14px;font-weight:700;color:var(--blue);margin-top:2px}
.prod .view{display:inline-block;margin-top:12px;background:var(--blue);color:var(--white);font-size:9px;padding:6px 14px;text-transform:uppercase}
.prod .calc{display:inline-block;margin-top:10px;border:1px solid var(--blue);color:var(--blue);font-size:8.5px;padding:5px 6px;text-transform:uppercase;white-space:nowrap}

/* testimonials */
.clients{top:3903px;height:536px;background:linear-gradient(180deg,#f3f4f6 0%,#ecedef 100%)}
.clients .h2{top:74px}
.quote-box{position:absolute;left:258px;top:156px;width:684px;height:318px;border:3px solid #bfbfbf;text-align:center}
.quote-box .q{font-family:"Montserrat",sans-serif;font-size:30px;font-weight:800;color:var(--blue);line-height:0;vertical-align:-12px}
.quote-box .q.open{position:absolute;left:44px;top:44px;line-height:1}
.quote-box p{margin:60px 70px 0;font-size:14px;line-height:22.5px;color:#333}
.quote-box .rule{width:28px;height:2px;background:var(--blue);margin:30px auto 14px}
.quote-box .who{font-family:"Montserrat",sans-serif;font-size:13px;font-weight:600;color:var(--blue);text-transform:uppercase}
.arrow{position:absolute;top:300px;width:16px;height:26px}

/* footer */
.site-footer{top:4439px;height:404px;background:var(--footer);color:#cfcfcf}
.foot-brand{position:absolute;left:132px;top:160px;width:300px}
.foot-brand .brand-name{font-size:26px;color:var(--blue)}
.foot-brand .tag{font-size:10px;letter-spacing:3px;color:#7f8a94;margin-top:12px;text-transform:uppercase;white-space:nowrap}
.foot-col{position:absolute;top:60px}
.foot-col h4{font-family:"Montserrat",sans-serif;font-size:14px;font-weight:700;color:var(--white);text-transform:uppercase;margin-bottom:24px}
.foot-col ul{list-style:none;font-size:13px;line-height:24.5px;text-transform:uppercase}
.row{display:flex;gap:14px;align-items:center;margin-bottom:22px;font-size:13px;line-height:19px}
.row .dot{width:30px;height:30px;border-radius:50%;background:var(--white);flex:none;display:flex;align-items:center;justify-content:center}
.row .dot svg{width:14px;height:14px}
.foot-line{position:absolute;left:122px;top:347px;width:956px;height:1px;background:#3a3a3c}
.copy{position:absolute;top:368px;left:0;width:1200px;text-align:center;font-size:10px;color:#aaa}
</style>
</head>
<body>

<header class="hero">
  <div class="photo" role="img" aria-label="Large grey-sided colonial house with new roof and landscaped lawn"></div>
  <div class="brand"><span class="brand-mark"></span><span class="brand-name">KEYSTONE ROOFING</span></div>
  <div class="brand-tag">Sturdy · Honest · Lasting</div>
  <div class="follow">FOLLOW US<div class="dots"><span></span><span></span><span></span></div></div>
  <div class="call">CALL TODAY FOR A FREE QUOTE!
    <div class="num"><svg viewBox="0 0 22 22"><circle cx="11" cy="11" r="11" fill="#1e8ddb"/><path d="M7.5 6.5c.6-.6 1.3-.5 1.6 0l1 1.6c.3.5.2 1-.2 1.3l-.6.5c.5 1.2 1.6 2.3 2.8 2.8l.5-.6c.3-.4.8-.5 1.3-.2l1.6 1c.5.3.6 1 0 1.6-.9.9-2.200 1-3.6.2-1.8-1-3.2-2.4-4.2-4.200-.8-1.4-.7-2.7.2-3.6z" fill="#fff"/></svg>555.014.2290</div>
  </div>
  <nav class="nav"><span class="active">Home</span><span>About</span><span>Services</span><span>Blog</span><span>Reviews</span><span>Projects</span><span>Contact Us</span></nav>
  <h1>BUILT RIGHT, BUILT TO LAST</h1>
  <div class="btn">Get an Instant Estimate</div>
</header>

<section class="services">
  <div class="h2">Services</div>
  <div class="svc" style="left:173px">
    <div class="ic"><svg viewBox="0 0 54 54" fill="none" stroke="#fff" stroke-width="3"><path d="M8 16l10-6 10 6 10-6 8 5v28l-8-5-10 6-10-6-10 6z"/><path d="M18 10v28M28 16v28M38 10v28"/></svg></div>
    <h3>ROOF INSTALLATION</h3>
  </div>
  <div class="svc" style="left:466px">
    <div class="ic"><svg viewBox="0 0 54 54" fill="none" stroke="#fff" stroke-width="4" stroke-linecap="round"><path d="M12 42l18-18M34 10a8 8 0 0 0 10 10l-6 6-10-10z"/><path d="M14 12l28 28"/></svg></div>
    <h3>ROOF REPAIR</h3>
  </div>
  <div class="svc" style="left:756px">
    <div class="ic"><svg viewBox="0 0 54 54" fill="#fff"><path d="M6 30l21-16 21 16-3 3-18-13-18 13z"/><rect x="15" y="31" width="24" height="14"/><rect x="36" y="10" width="6" height="12"/></svg></div>
    <h3>ADDITIONAL SERVICES</h3>
    <p>Windows/Skylights, Gutters, Siding,<br>Interior leak damage repairs</p>
  </div>
</section>

<section class="about">
  <div class="photo" role="img" aria-label="Aerial view of a white farmhouse with dark roof and terraced patio"></div>
  <h2>ABOUT US</h2>
  <p>After over a decade of general contracting, we continue to see a repetitive trend by the roof purchase process where homeowners are constantly left confused, nervous, and worried when they need a new roof. As one of the most important features of keeping your home safe, this is unacceptable. Keystone Roofing was created to break this trend.</p>
  <div class="btn">Read More</div>
</section>

<section class="roofs">
  <div class="h2">Types of Roofs</div>
  <div class="tile" style="left:132px;top:137px;width:299px;height:247px;background:linear-gradient(160deg,#b7b0a6,#7a6a58 60%,#4b3f33)" role="img" aria-label="Curved cedar shake roof"><span>CEDAR</span></div>
  <div class="tile" style="left:451px;top:137px;width:298px;height:247px;background:linear-gradient(180deg,#c9ccd0 0%,#a9adb2 35%,#3c3f44 60%,#26282c)" role="img" aria-label="Dark metal roof with white cupola"><span>METAL</span></div>
  <div class="tile" style="left:769px;top:137px;width:299px;height:247px;background:linear-gradient(160deg,#dfe2e5,#a8acb0 50%,#7c8085)" role="img" aria-label="Grey asphalt shingle gable"><span>ASPHALT</span></div>
  <div class="tile" style="left:132px;top:405px;width:455px;height:244px;background:linear-gradient(170deg,#e9c99a 0%,#9fb0c4 30%,#4a5e78 60%,#2c3a4f)" role="img" aria-label="Slate roof under sunset sky"><span>SLATE</span></div>
  <div class="tile" style="left:611px;top:405px;width:455px;height:244px;background:linear-gradient(160deg,#d4dbe2,#9ba5ae 40%,#6a7f5c 75%,#4c6a3e)" role="img" aria-label="White house with dark rubber roof"><span>RUBBER</span></div>
</section>

<section class="projects">
  <div class="h2">Recent Projects</div>
  <div class="grid">
    <div class="photo" style="background:linear-gradient(180deg,#b9c4cf,#8e969b 50%,#5c6a52)" role="img" aria-label="Grey shingled home with garage"></div>
    <div class="photo" style="background:linear-gradient(180deg,#3d4147,#2a2d31 60%,#1c1e21)" role="img" aria-label="Darkened house photo with project label"><span class="tag">PROJECT 1</span></div>
    <div class="photo" style="background:linear-gradient(180deg,#c7d0da,#a88f6f 50%,#6d7a56)" role="img" aria-label="Stone and shingle home with arched entry"></div>
    <div class="photo" style="background:linear-gradient(180deg,#1f4d9a,#3b6bb8 40%,#6f7780 70%,#3d4a3a)" role="img" aria-label="Coastal home under deep blue sky"></div>
    <div class="photo" style="background:linear-gradient(180deg,#9fb3c5,#5a7045 50%,#3e5531)" role="img" aria-label="Home behind tall trees with brick walkway"></div>
    <div class="photo" style="background:linear-gradient(180deg,#c8ccd1,#8c7c6a 50%,#e8e8e8)" role="img" aria-label="Cedar roof turret and white railing"></div>
    <div class="photo" style="background:linear-gradient(180deg,#7f9bb8,#a8b9ca 40%,#3b3e43 75%)" role="img" aria-label="Cupola with weathervane on dark roof"></div>
    <div class="photo" style="background:linear-gradient(180deg,#6f8c5a,#5b6e6c 50%,#43593a)" role="img" aria-label="Green-sided home among trees"></div>
  </div>
  <div class="btn">View All Projects</div>
</section>

<section class="estimate">
  <div class="h2">Instant Estimate</div>
  <div class="steps">
    <div class="step on"><i>1</i>Product Selection</div>
    <div class="step"><i>2</i>About Your Roof</div>
    <div class="step"><i>3</i>Roof Condition</div>
    <div class="step"><i>4</i>Get Your Cost</div>
  </div>
  <h3>Step 1: Pick Your Brand &amp; Shingle</h3>
  <div class="products">
    <div class="prod"><div class="photo" style="background:linear-gradient(180deg,#8b8d90,#5b5d61)" role="img" aria-label="Grey architectural shingle sample"></div><div class="body"><div class="tier">Good</div><div class="name">Ridgeline Classic</div><div class="price">$$$</div><span class="view">View Info</span><br><span class="calc">Calculate Your Cost</span></div></div>
    <div class="prod"><div class="photo" style="background:linear-gradient(180deg,#7d7f83,#4f5155)" role="img" aria-label="Dark shingle sample"></div><div class="body"><div class="tier">Better</div><div class="name">Ridgeline Meadow</div><div class="price">$$$</div><span class="view">View Info</span><br><span class="calc">Calculate Your Cost</span></div></div>
    <div class="prod"><div class="photo" style="background:linear-gradient(180deg,#7b8ca4,#4d5d77)" role="img" aria-label="Blue-grey shingle sample"></div><div class="body"><div class="tier">Best</div><div class="name">Ridgeline Elite</div><div class="price">$$$</div><span class="view">View Info</span><br><span class="calc">Calculate Your Cost</span></div></div>
    <div class="prod"><div class="photo" style="background:linear-gradient(180deg,#75767a,#45464a)" role="img" aria-label="Charcoal shingle sample"></div><div class="body"><div class="tier">Good</div><div class="name">Harbor Crest</div><div class="price">$$$</div><span class="view">View Info</span><br><span class="calc">Calculate Your Cost</span></div></div>
    <div class="prod"><div class="photo" style="background:linear-gradient(180deg,#3b3d40,#141517)" role="img" aria-label="Black tile sample"></div><div class="body"><div class="tier">Better</div><div class="name">Harbor Crest<br>Select</div><div class="price">$$$</div><span class="view">View Info</span><br><span class="calc">Calculate Your Cost</span></div></div>
    <div class="prod"><div class="photo" style="background:linear-gradient(180deg,#86888b,#57595c)" role="img" aria-label="Weathered grey shingle sample"></div><div class="body"><div class="tier">Better</div><div class="name">Harbor Crest<br>Reserve</div><div class="price">$$$</div><span class="view">View Info</span><br><span class="calc">Calculate Your Cost</span></div></div>
  </div>
</section>

<section class="clients">
  <div class="h2">Happy Clients</div>
  <svg class="arrow" style="left:200px" viewBox="0 0 16 26"><path d="M13 2L3 13l10 11" fill="none" stroke="#999" stroke-width="2"/></svg>
  <svg class="arrow" style="left:972px" viewBox="0 0 16 26"><path d="M3 2l10 11L3 24" fill="none" stroke="#999" stroke-width="2"/></svg>
  <div class="quote-box">
    <span class="q open">“</span>
    <p>We needed to put a new roof on our house, as well as repair a sagging porch roof. Shingles had been flying off and we had had several leaks. Owen provided a very reasonable estimate - well below some of the other Local Pro List companies. The work was done very promptly and professionally. A couple of issues that arose were settled to our satisfaction and Owen took full ownership of the situation. It was very clear that customer satisfaction is a priority for this company. I would definitely recommend and hire again <span class="q">”</span></p>
    <div class="rule"></div>
    <div class="who">Dan, Fairview</div>
  </div>
</section>

<footer class="site-footer">
  <div class="foot-brand"><div class="brand-name">KEYSTONE ROOFING</div><div class="tag">Sturdy — Honest — Lasting</div></div>
  <div class="foot-col" style="left:471px"><h4>Menu</h4>
    <ul><li>Home</li><li>About</li><li>Services</li><li>Blog</li><li>Reviews</li><li>Projects</li><li>Contact Us</li></ul></div>
  <div class="foot-col" style="left:616px"><h4>Contact Us</h4>
    <div class="row"><span class="dot"><svg viewBox="0 0 14 14"><path d="M7 1a4 4 0 0 0-4 4c0 3 4 8 4 8s4-5 4-8a4 4 0 0 0-4-4z" fill="#1f1f21"/><circle cx="7" cy="5" r="1.5" fill="#fff"/></svg></span><span>48 Orchard Ln.<br>Fairview MA 01999</span></div>
    <div class="row"><span class="dot"><svg viewBox="0 0 14 14"><path d="M3 2c.5-.5 1.1-.4 1.4 0l1 1.5c.3.4.2.9-.2 1.2l-.5.4c.5 1.2 1.4 2.1 2.6 2.6l.4-.5c.3-.4.8-.5 1.2-.2l1.5 1c.4.3.5.9 0 1.4-.9.9-2.2.9-3.5.1C5.2 8.4 4 7.2 3 5.5 2.2 4.2 2.2 2.9 3 2z" fill="#1f1f21"/></svg></span><span>Call Us<br>555-014-2290</span></div>
    <div class="row"><span class="dot"><svg viewBox="0 0 14 14"><rect x="1.5" y="3" width="11" height="8" fill="#1f1f21"/><path d="M1.5 3l5.5 4.5L12.5 3" fill="none" stroke="#fff" stroke-width="1"/></svg></span><span>E mail Us<br>owen@keystoneroofingco.com</span></div>
  </div>
  <div class="foot-col" style="left:934px"><h4>Follow Us</h4>
    <div class="row"><span class="dot"></span><span>Like us on<br>PAGEFEED</span></div>
    <div class="row"><span class="dot"></span><span>Follow us on<br>CHIRPLINE</span></div>
    <div class="row"><span class="dot"></span><span>Follow us on<br>WORKLINK</span></div>
  </div>
  <div class="foot-line"></div>
  <div class="copy">Copyright © 2020 All Rights Reserved</div>
</footer>

</body>
</html>
```